Harborline Cremations Business Cards

To create a business card for my company Harborline Cremations. Remember it is a cremation company.
We want to make sure people have a business card and information. Something modern, professional
100% Online
Prices starting at $695 all-inclusive (prices subject to change without notice).
A business card is the first point of contact with the prospective client.

Contact Information for Business Card

(305) 418-7260
www.HarborlineCremationsMiami.example
harborlinecremations@mailbox.example

Requirements
Must have
• 100% Online
Prices starting at $695 all-inclusive (prices subject to change without notice)

(305) 418-7260

Must match logo style
Should not have
• No black backgrounds. Please only use the white, orange and blue from the logo

```html
<!DOCTYPE html>
<html lang="en">
<head>
<meta charset="utf-8">
<title>Harborline Cremations – Business Cards</title>
<link rel="stylesheet" href="https://fonts.googleapis.com/css2?family=Montserrat:wght@400;500;700;800&display=swap">
<style>
  :root {
    --card-blue: #0aa2df;
    --sun-orange: #f28a2c;
    --white: #ffffff;
    --backdrop: #e9edf0;
  }
  * { box-sizing: border-box; margin: 0; padding: 0; }
  html, body { width: 1200px; height: 913px; overflow: hidden; }
  body {
    background: var(--backdrop);
    font-family: "Montserrat", Arial, sans-serif;
    color: var(--white);
    display: flex;
    flex-direction: column;
    align-items: center;
    justify-content: center;
    gap: 30px;
  }
  .card {
    position: relative;
    width: 720px;
    height: 411px;
    background: var(--card-blue);
    border-radius: 22px;
    box-shadow: 0 6px 18px rgba(0, 60, 90, 0.18);
    overflow: hidden;
  }
  .brand {
    display: flex;
    align-items: center;
    gap: 16px;
  }
  .brand-dot {
    flex: none;
    border-radius: 50%;
    background: var(--sun-orange);
  }
  .brand-name {
    font-weight: 700;
    color: var(--white);
    letter-spacing: 0.04em;
    line-height: 1.05;
    text-transform: uppercase;
  }
  /* Front */
  .card-front .brand {
    position: absolute;
    left: 50%;
    top: 50%;
    transform: translate(-50%, -50%);
  }
  .card-front .brand-dot { width: 84px; height: 84px; }
  .card-front .brand-name { font-size: 40px; }
  /* Back */
  .card-back .brand {
    position: absolute;
    left: 48px;
    top: 92px;
  }
  .card-back .brand-dot { width: 58px; height: 58px; }
  .card-back .brand-name { font-size: 27px; }
  .contact-list {
    position: absolute;
    left: 48px;
    bottom: 40px;
    list-style: none;
    display: flex;
    flex-direction: column;
    gap: 8px;
    font-size: 15px;
    font-weight: 400;
  }
  .contact-list li { display: flex; align-items: center; gap: 10px; }
  .contact-icon { width: 18px; height: 18px; flex: none; }
  .price-badge {
    position: absolute;
    right: 20px;
    top: 30px;
    width: 300px;
    height: 300px;
  }
  .badge-arc { font-weight: 500; font-size: 21px; letter-spacing: 0.08em; fill: var(--white); }
  .badge-online { font-weight: 700; font-size: 20px; fill: var(--white); }
  .badge-price { font-weight: 800; font-size: 76px; fill: var(--white); }
  .badge-note { font-weight: 500; font-size: 8.5px; fill: var(--white); }
</style>
</head>
<body>

<section class="card card-front" aria-label="Business card front">
  <div class="brand">
    <span class="brand-dot"></span>
    <span class="brand-name">Harborline<br>Cremations</span>
  </div>
</section>

<section class="card card-back" aria-label="Business card back">
  <div class="brand">
    <span class="brand-dot"></span>
    <span class="brand-name">Harborline<br>Cremations</span>
  </div>

  <ul class="contact-list">
    <li>
      <svg class="contact-icon" viewBox="0 0 24 24" aria-hidden="true"><path fill="#fff" d="M6.6 10.8a15.1 15.1 0 0 0 6.6 6.6l2.2-2.2c.3-.3.7-.4 1-.2 1.1.4 2.3.6 3.6.6.6 0 1 .4 1 1V20c0 .6-.4 1-1 1A17 17 0 0 1 3 4c0-.6.4-1 1-1h3.5c.6 0 1 .4 1 1 0 1.3.2 2.5.6 3.6.1.3 0 .7-.2 1z"/></svg>
      <span>(305) 418-7260</span>
    </li>
    <li>
      <svg class="contact-icon" viewBox="0 0 24 24" aria-hidden="true"><rect x="2" y="5" width="20" height="14" rx="1.5" fill="#fff"/><path d="M3 6l9 7 9-7" fill="none" stroke="#0aa2df" stroke-width="1.8"/></svg>
      <span>harborlinecremations@mailbox.example</span>
    </li>
    <li>
      <svg class="contact-icon" viewBox="0 0 24 24" aria-hidden="true"><circle cx="12" cy="12" r="10" fill="#fff"/><path d="M2 12h20M12 2c3 3 3 17 0 20M12 2c-3 3-3 17 0 20" fill="none" stroke="#0aa2df" stroke-width="1.4"/></svg>
      <span>www.HarborlineCremationsMiami.example</span>
    </li>
  </ul>

  <svg class="price-badge" viewBox="0 0 300 300" aria-label="Prices starting at $695, 100% Online, all-inclusive">
    <defs>
      <path id="arc-top" d="M 28 150 A 122 122 0 0 1 272 150"/>
      <path id="arc-bottom" d="M 14 150 A 136 136 0 0 0 286 150"/>
    </defs>
    <text class="badge-arc"><textPath href="#arc-top" startOffset="50%" text-anchor="middle">PRICES STARTING AT</textPath></text>
    <text class="badge-arc"><textPath href="#arc-bottom" startOffset="50%" text-anchor="middle">ALL-INCLUSIVE</textPath></text>
    <text class="badge-online" x="150" y="108" text-anchor="middle">100% Online</text>
    <text class="badge-price" x="150" y="180" text-anchor="middle">$695</text>
    <text class="badge-note" x="150" y="204" text-anchor="middle">*prices subject to change without notice</text>
  </svg>
</section>

</body>
</html>
```